Remodel Flyer for realtors

"K" Tandem Builders

4"x 9" rack card front and back

www.BrindleyRenovator.com

555-318-4762

Let us fix what your home inspector finds!

Send us your inspection summary.

We are a licensed and Insured contractor.
CRC4871093

Serving
Marion County and The Heronfield

This flyer will sit in realtor offices for realtors to give to there buyers and sellers.

Target Market(s)

Realtors

Industry/Entity Type

Construction

Colors

Designer to choose colors to be used in the design.

```html
<!DOCTYPE html>
<html lang="en">
<head>
<meta charset="utf-8">
<title>K Tandem Builders – Rack Card</title>
<link href="https://fonts.googleapis.com/css2?family=Roboto:wght@400;500;700&family=Saira+Condensed:wght@500;600;700&display=swap" rel="stylesheet">
<style>
  :root {
    --stage: #55575a;
    --orange: #f3931f;
    --orange-light: #f7ad55;
    --charcoal: #4a4c4f;
    --white: #ffffff;
    --text-dark: #4d4f52;
  }
  html, body {
    margin: 0;
    padding: 0;
    width: 1161px;
    height: 1200px;
    overflow: hidden;
    background: var(--stage);
  }
  .canvas {
    position: relative;
    width: 1161px;
    height: 1200px;
  }
  .card {
    position: absolute;
    top: 44px;
    width: 490px;
    height: 1102px;
    background: var(--white);
    box-shadow: 0 2px 8px rgba(0,0,0,0.25);
  }
  .card--front { left: 78px; }
  .card--back { left: 610px; width: 494px; }
  .card svg { display: block; width: 100%; height: 100%; }

  .fill-orange { fill: var(--orange); }
  .fill-charcoal { fill: var(--charcoal); }
  .fill-white { fill: var(--white); }

  .brand-name {
    font-family: 'Saira Condensed', sans-serif;
    font-weight: 700;
    font-size: 50px;
    fill: var(--charcoal);
    letter-spacing: 1px;
  }
  .badge-text {
    font-family: 'Roboto', sans-serif;
    font-weight: 500;
    font-size: 18px;
    fill: var(--white);
  }
  .badge-license {
    font-family: 'Roboto', sans-serif;
    font-weight: 700;
    font-size: 24px;
    fill: var(--white);
  }
  .front-url {
    font-family: 'Roboto', sans-serif;
    font-weight: 700;
    font-size: 38px;
    fill: var(--orange);
  }
  .front-phone {
    font-family: 'Roboto', sans-serif;
    font-weight: 700;
    font-size: 40px;
    fill: var(--white);
  }
  .headline {
    font-family: 'Saira Condensed', sans-serif;
    font-weight: 600;
    font-size: 38px;
    fill: var(--white);
    letter-spacing: 1.5px;
  }
  .back-name {
    font-family: 'Saira Condensed', sans-serif;
    font-weight: 700;
    font-size: 52px;
    fill: var(--orange);
  }
  .serving-title {
    font-family: 'Roboto', sans-serif;
    font-weight: 700;
    font-size: 52px;
    fill: var(--white);
  }
  .serving-area {
    font-family: 'Roboto', sans-serif;
    font-weight: 500;
    font-size: 30px;
    fill: var(--white);
  }
  .summary-line {
    font-family: 'Roboto', sans-serif;
    font-weight: 500;
    font-size: 30px;
    fill: var(--orange);
  }
  .back-contact {
    font-family: 'Roboto', sans-serif;
    font-weight: 700;
    font-size: 40px;
    fill: var(--text-dark);
  }
</style>
</head>
<body>
<div class="canvas">

  <!-- Front of rack card -->
  <section class="card card--front">
    <svg viewBox="0 0 613 1377" preserveAspectRatio="none" xmlns="http://www.w3.org/2000/svg">
      <defs>
        <linearGradient id="roomTone" x1="0" y1="0" x2="0" y2="1">
          <stop offset="0" stop-color="#eee9e0"/>
          <stop offset="0.35" stop-color="#d9b874"/>
          <stop offset="0.7" stop-color="#c8b79a"/>
          <stop offset="1" stop-color="#b8642a"/>
        </linearGradient>
        <linearGradient id="badgeTone" x1="0" y1="0" x2="0" y2="1">
          <stop offset="0" stop-color="#f7b261"/>
          <stop offset="1" stop-color="#f39426"/>
        </linearGradient>
      </defs>

      <!-- brand -->
      <g class="brand">
        <rect class="fill-orange" x="80" y="188" width="40" height="40"/>
        <text class="brand-name" x="135" y="226">K TANDEM BUILDERS</text>
      </g>

      <!-- top swooshes -->
      <path class="fill-charcoal" d="M0,315 C160,225 450,215 613,345 L613,362 C450,265 160,290 0,400 Z"/>
      <path class="fill-orange" d="M0,462 C160,330 450,300 613,372 L613,398 C450,335 160,362 0,500 Z"/>

      <!-- room photograph area -->
      <path role="img" aria-label="Photo of a bright living room with white sofas and hardwood floor"
            fill="url(#roomTone)"
            d="M0,515 C160,380 450,345 613,405 L613,925 C450,1000 160,985 0,928 Z"/>

      <!-- bottom swooshes -->
      <path class="fill-orange" d="M0,928 C160,985 450,1000 613,925 L613,952 C450,1030 160,1015 0,950 Z"/>
      <path class="fill-charcoal" d="M0,945 C200,1025 450,1035 613,975 L613,1058 C450,1095 230,1060 0,985 Z"/>
      <path class="fill-orange" d="M0,1000 C230,1080 450,1110 613,1070 L613,1205 L0,1205 Z"/>

      <!-- license badge -->
      <g class="license-badge">
        <path fill="url(#badgeTone)" d="M100,1085 L100,1010 C100,955 160,930 225,930 C290,930 350,955 350,1010 L350,1085 Z"/>
        <text class="badge-text" x="225" y="1000" text-anchor="middle">We are a licensed and</text>
        <text class="badge-text" x="225" y="1022" text-anchor="middle">Insured contractor.</text>
        <text class="badge-license" x="225" y="1060" text-anchor="middle">CRC4871093</text>
      </g>

      <!-- contact bands -->
      <rect class="fill-white" x="0" y="1205" width="613" height="75"/>
      <text class="front-url" x="306" y="1257" text-anchor="middle">www.BrindleyRenovator.com</text>
      <rect class="fill-orange" x="0" y="1280" width="613" height="97"/>
      <text class="front-phone" x="306" y="1337" text-anchor="middle">555-318-4762</text>
    </svg>
  </section>

  <!-- Back of rack card -->
  <section class="card card--back">
    <svg viewBox="0 0 617 1377" preserveAspectRatio="none" xmlns="http://www.w3.org/2000/svg">
      <defs>
        <linearGradient id="bathTone" x1="0" y1="0" x2="1" y2="1">
          <stop offset="0" stop-color="#f1f1ee"/>
          <stop offset="0.4" stop-color="#c9d3c4"/>
          <stop offset="0.7" stop-color="#8a7a6c"/>
          <stop offset="1" stop-color="#d9cbb8"/>
        </linearGradient>
      </defs>

      <!-- bathroom photograph area -->
      <path role="img" aria-label="Photo of a remodeled bathroom with dark vanity and large windows"
            fill="url(#bathTone)"
            d="M0,0 L617,0 L617,470 C500,590 300,680 0,630 Z"/>

      <!-- swooshes beneath photo -->
      <path class="fill-orange" d="M0,630 C300,680 500,590 617,470 L617,530 C500,640 300,700 0,650 Z"/>
      <path class="fill-white" d="M0,650 C300,700 500,640 617,530 L617,580 C500,680 300,715 0,660 Z"/>
      <path class="fill-charcoal" d="M0,640 C200,730 450,740 617,590 L617,645 C450,765 220,760 0,690 Z"/>

      <!-- headline banner -->
      <rect x="0" y="103" width="490" height="98" fill="#f3931f" fill-opacity="0.82"/>
      <text class="headline" x="45" y="142">Let us fix what your home</text>
      <text class="headline" x="45" y="186">inspector finds!</text>

      <!-- company name -->
      <text class="back-name" x="315" y="842" text-anchor="middle">"K" Tandem Builders</text>

      <!-- service area band -->
      <rect class="fill-orange" x="0" y="905" width="617" height="142"/>
      <line x1="0" y1="949" x2="210" y2="949" stroke="#ffffff" stroke-width="2"/>
      <line x1="408" y1="949" x2="617" y2="949" stroke="#ffffff" stroke-width="2"/>
      <text class="serving-title" x="309" y="966" text-anchor="middle">Serving</text>
      <text class="serving-area" x="314" y="1018" text-anchor="middle">Marion County and The Heronfield</text>

      <!-- call to action -->
      <text class="summary-line" x="310" y="1142" text-anchor="middle">Send us your inspection summary.</text>

      <!-- contact -->
      <text class="back-contact" x="313" y="1258" text-anchor="middle">www.BrindleyRenovator.com</text>
      <text class="back-contact" x="313" y="1337" text-anchor="middle">555-318-4762</text>
    </svg>
  </section>

</div>
</body>
</html>
```